Small consulting business needs a website designed to highlight value and four offerings

My company is a dynamic consulting firm with four Core Offerings: Learning & Evaluation, Program Management, Facilitation & Coaching; Implementation & Transformation. Our mission is to facilitate organizational change and transformation, and to make space for creativity, joy, belonging, and trust. If done successfully, we grow to better understand ourselves, each other, and the work we do together.

I'd like the website to give a feeling of confidence and clarity. I want the colors to match or compliment my logo. I want to have three tabs - Our Clients, Our Services, and Government.

See attached Word document for additional content. My current website is www.BrightHeronWorks.com.

Some websites I'm inspired by:
https://www.velmorgrove.com
https://www.tandemoakpartners.com
https://qzrb.org

Some websites of people/groups in my field that I find uninspiring:
http://dianacolfax.com
https://www.marbleway.org

Target Market(s)

State and local government agencies, health tech, and corporate HR departments

Industry/Entity Type

public health, aging, government, health tech

Coding

Coded - Design and coding required

Number of Pages Required

4 page

Font styles to use
Other font styles liked:
• Calibri and Merriweather

Colors
0054AA
0677BA
7BADD7
CADEEF
E8F1F8
00AB8E
00BBA5
67D7C9
C6EFE9
E9F9F6
FFC000
F8CF3A
FAE287
FDF2CF
FEFAEE
F0912C
F2A743
F7CA91
FBE8D2
FDF5EE

Requirements
Must have
• Attached logo and content, water colors few, and photos.
Nice to have
• Real pictures, which I can provide to the chosen designer
Should not have
• AI generated characters or cartoons.

```html
<!DOCTYPE html>
<html lang="en">
<head>
<meta charset="utf-8">
<title>Bright Heron Works</title>
<link href="https://fonts.googleapis.com/css2?family=Lora:wght@400;500;600;700&family=Roboto:wght@300;400;500&display=swap" rel="stylesheet">
<style>
:root{
  --cream:#fdf9ea;
  --band:#fcefc6;
  --ink:#173a3a;
  --body:#3a3a3a;
  --orange:#f0912c;
  --orange-deep:#e17e1a;
  --faded:#f0d592;
  --pill:#ebe1c6;
  --pill-text:#7a7566;
  --teal:#2f7f73;
  --gold:#f3b32a;
}
*{margin:0;padding:0;box-sizing:border-box}
html,body{width:1200px;height:5025px;overflow:hidden}
body{
  position:relative;
  background:
    radial-gradient(circle at 0px 300px,rgba(247,170,140,.35),transparent 160px),
    radial-gradient(circle at 1200px 1450px,rgba(250,226,135,.45),transparent 150px),
    radial-gradient(circle at 0px 1150px,rgba(247,202,145,.45),transparent 140px),
    radial-gradient(circle at 20px 1880px,rgba(200,220,120,.35),transparent 130px),
    radial-gradient(circle at 1200px 2400px,rgba(247,170,140,.3),transparent 150px),
    radial-gradient(circle at 1190px 3900px,rgba(200,220,120,.3),transparent 140px),
    radial-gradient(circle at 10px 3980px,rgba(247,202,145,.4),transparent 140px),
    var(--cream);
  font-family:'Roboto',Arial,sans-serif;
  color:var(--body);
}
.abs{position:absolute}
.center{left:0;width:1200px;text-align:center}
.serif{font-family:'Lora',Georgia,serif}

/* header */
.brand{left:36px;top:20px;display:flex;align-items:center;gap:14px}
.brand-mark{width:42px;height:42px;border-radius:50%;background:var(--gold)}
.brand-name{font-family:'Lora',Georgia,serif;font-size:15px;line-height:19px;color:#1f1f1f;text-align:center}
.nav{top:36px;left:390px;display:flex;gap:26px;align-items:center;font-size:13.5px;color:#222;list-style:none}
.nav .active{background:var(--orange);color:#fff;padding:4px 14px;border-radius:14px}

/* hero */
.hero-title{top:124px;font-size:39px;line-height:57px;color:var(--ink)}
.hero-title b{color:var(--orange);font-weight:700}
.hero-sub{top:262px;font-size:15.5px;line-height:26px;color:#333}
.hero-sub b{color:var(--orange);font-weight:500}
.offer-art{left:330px;top:352px;width:540px;height:518px;border-radius:50%;
  background:radial-gradient(circle,#e3b52c 0%,#9aa84a 40%,#3d8a76 70%,rgba(253,249,234,0) 72%)}

.section-h{font-size:39px;color:var(--ink);font-weight:400}
.scroll-cue{left:584px;top:1040px}

/* mission blocks */
.rule{height:2px;background:#2c4b4b}
.badge{left:569px;width:62px;height:62px;border-radius:50%;background:#c5631a;display:flex;align-items:center;justify-content:center}
.para{font-size:15.5px;line-height:25.5px;color:#333}

.art{border-radius:50%}
.art-rings{left:150px;top:1950px;width:410px;height:380px;
  background:radial-gradient(circle at 45% 50%,#d7a93a 0%,#8a9a52 40%,#2c6e6a 62%,rgba(253,249,234,0) 72%)}
.art-burst{left:640px;top:1950px;width:410px;height:380px;
  background:radial-gradient(circle,#fdf9ea 0%,#f0a030 30%,#2f7b5d 55%,rgba(253,249,234,0) 72%)}

/* band */
.band{left:0;width:1200px;background:var(--band)}
.help-line{font-family:'Lora',Georgia,serif;font-size:33px;color:var(--faded);display:inline-block;padding-bottom:6px;border-bottom:2px solid #f5e2ae}
.help-line.on{font-size:45px;color:var(--orange-deep);border-bottom-color:var(--orange)}
.short-rule{left:578px;width:44px;height:2px;background:var(--ink)}
.big{top:3112px;font-size:113px;line-height:140px;color:var(--ink);white-space:nowrap;letter-spacing:-1px}

/* collaborate */
.pill{left:50%;transform:translateX(-50%);font-family:'Lora',Georgia,serif;background:var(--pill);color:var(--pill-text);border-radius:8px;text-align:center;white-space:nowrap}
.pill.lead{background:var(--orange);color:#fff}

/* why */
.why-art{left:137px;top:4352px;width:450px;height:270px;border-radius:50% 50% 40% 40%;
  background:radial-gradient(ellipse at 50% 40%,#f3c04a 0%,#d59a35 35%,#4f8a7a 65%,rgba(252,239,198,0) 72%)}

/* footer */
.footer-mark{left:572px;top:4706px;width:56px;height:56px;border-radius:50%;background:var(--gold)}
.foot-nav{top:4896px;left:178px;display:flex;gap:0;width:844px;justify-content:space-between;font-size:15px;color:#222;list-style:none}
.social{display:flex;gap:6px}
.social span{width:22px;height:22px;border-radius:50%;background:var(--orange)}
</style>
</head>
<body>

<header>
  <div class="abs brand"><span class="brand-mark"></span><span class="brand-name">Bright Heron<br>Works</span></div>
  <ul class="abs nav">
    <li class="active">Home</li><li>About Us</li><li>Our Services</li><li>Government</li><li>Core Offerings</li><li>Clients</li><li>Case Studies</li><li>Contact us</li>
  </ul>
</header>

<section class="hero">
  <h1 class="abs center serif hero-title" style="font-weight:400">A Seat at the Table for <b>Collaboration,</b><br><b>Learning, and Meaningful</b> Change</h1>
  <p class="abs center hero-sub"><b>Bright Heron Works</b> is a dynamic consulting firm with four Core Offerings: Learning &amp; Evaluation,<br>Program Management, Facilitation &amp; Coaching; Implementation &amp; Transformation</p>
  <div class="abs offer-art" role="img" aria-label="Watercolor puzzle wheel of the four core offerings: Learning, Implementation, Facilitation, Program Management"></div>
</section>

<h2 class="abs center serif section-h" style="top:936px">Here for you and your team</h2>
<svg class="abs scroll-cue" width="32" height="56" viewBox="0 0 32 56" fill="none" stroke="#f0912c" stroke-width="2">
  <rect x="6" y="2" width="20" height="30" rx="10"/><line x1="16" y1="9" x2="16" y2="14"/>
  <line x1="16" y1="38" x2="16" y2="52"/><polyline points="10,46 16,52 22,46"/>
</svg>

<!-- mission -->
<div class="abs rule" style="left:146px;width:390px;top:1170px"></div>
<div class="abs rule" style="left:663px;width:390px;top:1170px"></div>
<div class="abs badge" style="top:1132px"><svg width="34" height="34" viewBox="0 0 34 34" fill="none" stroke="#fff" stroke-width="2"><circle cx="17" cy="17" r="13"/><circle cx="17" cy="17" r="8"/><circle cx="17" cy="17" r="3"/></svg></div>
<h2 class="abs center serif section-h" style="top:1212px">Our Mission</h2>
<p class="abs center para" style="top:1279px">Our mission is to facilitate organizational change and transformation, and to make<br>space for creativity, joy, belonging, and trust. If done successfully, we grow to better<br>understand ourselves, each other, and the work we do together.</p>

<!-- vision -->
<div class="abs rule" style="left:146px;width:390px;top:1405px"></div>
<div class="abs rule" style="left:663px;width:390px;top:1405px"></div>
<div class="abs badge" style="top:1374px"><svg width="34" height="34" viewBox="0 0 34 34" fill="none" stroke="#fff" stroke-width="2"><path d="M3 17 Q17 5 31 17 Q17 29 3 17Z"/><circle cx="17" cy="17" r="4"/></svg></div>
<h2 class="abs center serif section-h" style="top:1458px">Our Vision</h2>
<p class="abs center para" style="top:1525px">Our vision is to be part of a world where organizations and collaborators connect as human beings<br>first. We envision a future where partners and colleagues strive for ongoing growth together.</p>

<!-- value -->
<div class="abs rule" style="left:146px;width:390px;top:1633px"></div>
<div class="abs rule" style="left:663px;width:390px;top:1633px"></div>
<div class="abs badge" style="top:1602px"><svg width="34" height="34" viewBox="0 0 34 34" fill="none" stroke="#fff" stroke-width="2"><polygon points="6,12 11,6 23,6 28,12 17,28"/><line x1="6" y1="12" x2="28" y2="12"/></svg></div>
<h2 class="abs center serif section-h" style="top:1693px">Our Value</h2>
<p class="abs center para" style="top:1766px">We are the tranquility in chaos. The steady partner always at the table with you.<br>We drive meaningful and measurable change, resulting in sustained progress towards key community<br>outcomes and multi-sector initiatives. Our work produces values realignment, critical technical assistance,<br>and develops strategic plans for innovative organizations ready to elevate their work.</p>

<div class="abs art art-rings" role="img" aria-label="Watercolor of overlapping rings in gold and teal"></div>
<div class="abs art art-burst" role="img" aria-label="Watercolor burst of orange and green strokes"></div>

<!-- help band -->
<svg class="abs" style="left:0;top:2340px" width="1200" height="80" viewBox="0 0 1200 80" preserveAspectRatio="none"><path d="M0 60 C300 0 600 20 800 40 C1000 60 1100 30 1200 20 L1200 80 L0 80Z" fill="#fcefc6"/></svg>
<div class="abs band" style="top:2419px;height:800px"></div>
<h2 class="abs center serif section-h" style="top:2530px">We Help Your Team...</h2>
<div class="abs short-rule" style="top:2616px"></div>
<div class="abs center" style="top:2668px"><span class="help-line">Turn bold visions into practical results.</span></div>
<div class="abs center" style="top:2766px"><span class="help-line on">Transform conflict into opportunity.</span></div>
<div class="abs center" style="top:2880px"><span class="help-line">Strengthen community-led systems.</span></div>
<div class="abs center" style="top:2990px"><span class="help-line">Foster a sense of belonging...</span></div>
<div class="abs center serif big">...Find common ground.</div>

<!-- collaborate -->
<h2 class="abs center serif section-h" style="top:3310px">We Collaborate With</h2>
<div class="abs short-rule" style="top:3396px"></div>
<div class="abs pill lead" style="top:3448px;width:620px;height:76px;line-height:76px;font-size:40px">Large-scale Companies</div>
<div class="abs pill" style="top:3560px;width:500px;height:52px;line-height:52px;font-size:31px">National and local nonprofits</div>
<div class="abs pill" style="top:3652px;width:420px;height:46px;line-height:46px;font-size:26px">State government agencies</div>
<div class="abs pill" style="top:3738px;width:520px;height:44px;line-height:44px;font-size:24px">International Partnerships &amp; Organizations</div>
<div class="abs pill" style="top:3828px;width:190px;height:40px;line-height:40px;font-size:19px">Foundations</div>
<div class="abs pill" style="top:3904px;width:240px;height:34px;line-height:34px;font-size:15px">Tribal Serving-Organizations</div>
<div class="abs pill" style="top:3971px;width:130px;height:30px;line-height:30px;font-size:11px">Startups in tech</div>

<!-- why us band -->
<svg class="abs" style="left:0;top:4060px" width="1200" height="50" viewBox="0 0 1200 50" preserveAspectRatio="none"><path d="M0 30 C300 0 700 10 900 25 C1050 35 1150 20 1200 10 L1200 50 L0 50Z" fill="#fcefc6"/></svg>
<div class="abs band" style="top:4109px;height:563px"></div>
<div class="abs why-art" role="img" aria-label="Watercolor of a path leading toward a rising sun framed by leaves"></div>
<h2 class="abs serif section-h" style="left:632px;top:4194px">Why Us</h2>
<div class="abs" style="left:636px;top:4266px;width:44px;height:2px;background:var(--ink)"></div>
<p class="abs" style="left:636px;top:4308px;width:410px;font-size:16px;line-height:25.5px;color:#333">Through our Core Offerings and guided by our founder's traditional and nontraditional methods for engaging and steering a team, we create a sense of belonging, foster transparency, and help to build stronger relationships. Our approach helps to drive meaningful change so that organizations and initiatives can clear roadblocks and meet collective goals. Our team's proven ability to transform conflict into opportunity will help to advance your organization and the communities you serve.</p>

<!-- footer -->
<footer>
  <div class="abs footer-mark"></div>
  <div class="abs center serif" style="top:4790px;font-size:23px;line-height:33px;color:#1f1f1f">Bright Heron<br>Works</div>
  <div class="abs rule" style="left:148px;width:902px;top:4876px;background:#555;height:1px"></div>
  <ul class="abs foot-nav"><li>Home</li><li>About Us</li><li>Our Services</li><li>Government</li><li>Core Offerings</li><li>Clients</li><li>Case Studies</li><li>Contact us</li></ul>
  <div class="abs rule" style="left:148px;width:902px;top:4937px;background:#555;height:1px"></div>
  <div class="abs" style="left:150px;top:4966px;display:flex;align-items:center;gap:14px;font-size:13px;color:#222">Follow us <div class="social"><span></span><span></span><span></span><span></span><span></span></div></div>
  <div class="abs" style="left:780px;width:270px;text-align:right;top:4970px;font-family:'Lora',Georgia,serif;font-size:12px;color:#222">Copyright © 2025 All Rights Reserved</div>
</footer>

</body>
</html>
```